Cellar Legacies, a definitive reference book on port

My husband has just finished writing a big book on Vintage Port. We need a hardcover book flap design for this book that is impressively huge. It's taken 10 years to research and write. It's 650 pages, interior is A4, exterior 4mm larger, and weighs nearly 3 kilos. It's a special book for people in the wine and port industry, as well as for someone who loves to drink Vintage Port. It can be a beautiful coffeetable book too.

The book is mainly about port and its declared vintages. It's also about the history of port, who drank it, when, how, where, who bought it, for how much, and the port houses are also described in detail.

The wine expert Gerald Thornwick wrote a book about vintage wine in 2002, and my husband would like to have a similar cover for his book. (A photo attached in files). I've attached other photos to give the designers an idea of the look and feel of the 'port culture', as well as photos of the typeface that my husband will be using for the inside hardcover.

Target Market(s)

Wine and port industry. Wine aficionados.

Industry/Entity Type

Winery

Font styles to use
Sans Serif
Script

Colors
ec1f27
1b1b1b
474747
333333
5c5c5c
faa54b

Requirements
Must have
• Book Cover must have Title: "Cellar Legacies" and "R. T. K. Hollister" (files attached to show proper typeface). One of the files is a flap jacket book cover that my husband designed himself. We're looking for more design ideas, and that pdf is a close winner to what he wants.
Nice to have
• illustration or painting of port glasses, or grapes, or similar. Dark colors, especially port wine, deep red wine colors. Gold writing, black writing, with red/berry/maroon accents. Luxury, elegance, has a masculine edge, traditional, but not too old-school and boring (like grandpa). Textures that are including with the culture of drinking vintage port are leather, velvet, cigar, wood, marble, winter, fireplaces. This sounds quite heavy, but it also should be simple and clean. I hope this isn't too confusing. Thanks!
Should not have
• Bright colors, playfulness.

```html
<!DOCTYPE html>
<html lang="en">
<head>
<meta charset="utf-8">
<title>Cellar Legacies – Book Cover</title>
<link rel="stylesheet" href="https://fonts.googleapis.com/css2?family=Pinyon+Script&family=Montserrat:wght@400;600&family=Playfair+Display:wght@700&display=swap">
<style>
  :root {
    --stage: #1b1b1b;
    --cover: #2c0a1a;
    --cover-deep: #160510;
    --panel: rgba(96, 22, 34, 0.72);
    --gold: #c9a54e;
    --gold-soft: #d9b866;
    --berry: #d4626a;
    --initial: #c45a62;
    --ornament: #7e2230;
    --wine: #8e1522;
  }
  html, body {
    margin: 0;
    padding: 0;
    width: 1200px;
    height: 789px;
    overflow: hidden;
    background: var(--stage);
  }
  .canvas {
    position: relative;
    width: 1200px;
    height: 789px;
  }
  .cover {
    position: absolute;
    left: 360px;
    top: 44px;
    width: 480px;
    height: 700px;
    background: var(--cover);
    overflow: hidden;
  }
  .cover__photo {
    position: absolute;
    inset: 0;
    background:
      radial-gradient(ellipse 120px 70px at 330px 560px, rgba(176, 26, 40, 0.75), transparent 75%),
      radial-gradient(ellipse 150px 200px at 335px 470px, rgba(150, 90, 110, 0.28), transparent 72%),
      radial-gradient(ellipse 110px 40px at 130px 540px, rgba(120, 30, 45, 0.45), transparent 75%),
      radial-gradient(ellipse 60px 160px at 330px 300px, rgba(130, 70, 90, 0.18), transparent 75%),
      linear-gradient(180deg, #300b1c 0%, var(--cover) 45%, var(--cover-deep) 100%);
  }
  .title-panel {
    position: absolute;
    left: 67px;
    top: 38px;
    width: 354px;
    height: 402px;
  }
  .title-panel__frame {
    position: absolute;
    inset: 0;
  }
  .title-panel__crest {
    position: absolute;
    left: 137px;
    top: 26px;
    width: 80px;
    height: 12px;
    background: radial-gradient(ellipse at 50% 50%, #c65a62 0%, rgba(198, 90, 98, 0.4) 60%, transparent 100%);
    border-radius: 50%;
  }
  .book-title {
    position: absolute;
    left: 0;
    top: 58px;
    width: 354px;
    margin: 0;
    text-align: center;
    font-family: "Pinyon Script", cursive;
    font-weight: 400;
    font-size: 50px;
    line-height: 1.1;
    color: var(--gold-soft);
  }
  .book-subtitle {
    position: absolute;
    left: 0;
    top: 139px;
    width: 354px;
    margin: 0;
    text-align: center;
    font-family: "Montserrat", sans-serif;
    font-weight: 400;
    font-size: 15px;
    letter-spacing: 1px;
    color: var(--berry);
  }
  .title-panel__emblem {
    position: absolute;
    left: 42px;
    top: 180px;
    width: 270px;
    height: 205px;
    background: radial-gradient(ellipse 50% 50% at 50% 50%, rgba(150, 40, 52, 0.85) 0%, rgba(126, 34, 48, 0.6) 55%, transparent 100%);
  }
  .title-panel__initial {
    position: absolute;
    left: 0;
    top: 172px;
    width: 354px;
    margin: 0;
    text-align: center;
    font-family: "Playfair Display", serif;
    font-weight: 700;
    font-size: 150px;
    line-height: 1.2;
    color: var(--initial);
  }
  .book-author {
    position: absolute;
    left: 0;
    top: 602px;
    width: 480px;
    margin: 0;
    text-align: center;
    font-family: "Montserrat", sans-serif;
    font-weight: 600;
    font-size: 18px;
    letter-spacing: 2px;
    color: var(--gold);
  }
</style>
</head>
<body>
<main class="canvas">
  <section class="cover">
    <div class="cover__photo" role="img" aria-label="Dark cellar photograph of a port glass with swirling red wine beside a bunch of grapes"></div>

    <div class="title-panel">
      <svg class="title-panel__frame" width="354" height="402" viewBox="0 0 354 402" aria-hidden="true">
        <path d="M0 36 Q0 20 24 20 L118 20 Q138 20 148 8 Q177 -4 206 8 Q216 20 236 20 L330 20 Q354 20 354 36 L354 402 L0 402 Z"
              fill="var(--panel)"/>
        <path d="M10 48 Q10 34 28 34 L120 34 Q140 34 150 22 Q177 12 204 22 Q214 34 234 34 L326 34 Q344 34 344 48 L344 392 L10 392 Z"
              fill="none" stroke="var(--gold)" stroke-width="1"/>
      </svg>
      <div class="title-panel__crest" role="img" aria-label="Small ornamental flourish"></div>
      <h1 class="book-title">Cellar Legacies</h1>
      <p class="book-subtitle">THE ART OF PORT WINE</p>
      <div class="title-panel__emblem" role="img" aria-label="Ornamental scrollwork with a grape cluster around the initial"></div>
      <p class="title-panel__initial" aria-hidden="true">C</p>
    </div>

    <p class="book-author">R. T. K. Hollister</p>
  </section>
</main>
</body>
</html>
```